Law Firm in Texas in need of new letterhead

Law Firm in Fort Worth, TX, USA named "Pell & Whitcombe, Attorneys-At-Law, LLP." This is a general practice law firm that mostly does Family Law and Criminal Defense work.

We are looking for a new letterhead that has a "classical" appeal, with modern elements.

Any color combination is fine, but please note that we do fax many documents, so the design must be clearly legible in Black and White.

We would like our letterhead to project a sense of professionalism, integrity, and ability.

Target Market(s)

Letterhead will be for correspondence generally with other attorneys and clients.

Industry/Entity Type

Law Firm

Logo Text

Pell & Whitcombe, Attorneys-At-Law, LLP.

Logo styles of interest
Pictorial/Combination Logo
Wordmark Logo
Lettermark Logo
Requirements
Nice to have
• Although not necessary, a "Texas Star" that is incorporated into the design would be a nice touch.
Should not have
• Colors that do not convert to B&W easily

```html
<!DOCTYPE html>
<html lang="en">
<head>
<meta charset="utf-8">
<title>Pell &amp; Whitcombe Letterhead</title>
<link href="https://fonts.googleapis.com/css2?family=Carlito:wght@400;700&display=swap" rel="stylesheet">
<style>
  :root {
    --backdrop: #1e1e1e;
    --paper: #ffffff;
    --ink: #1a1a1a;
    --ink-soft: #333333;
    --rule: #222222;
    --watermark: #ececec;
    --watermark-edge: #e2e2e2;
  }
  * { box-sizing: border-box; margin: 0; padding: 0; }
  html, body { width: 1200px; height: 1000px; overflow: hidden; }
  body {
    background: var(--backdrop);
    font-family: "Carlito", "Calibri", sans-serif;
    color: var(--ink);
    position: relative;
  }
  .sheet {
    position: absolute;
    width: 532px;
    height: 755px;
    background: var(--paper);
    box-shadow: 0 4px 18px rgba(0,0,0,0.6);
    overflow: hidden;
  }
  .sheet--blank { left: 53px; top: 157px; }
  .sheet--letter { left: 622px; top: 155px; }

  .letterhead {
    position: absolute;
    left: 12px; right: 12px; top: 18px;
    height: 34px;
  }
  .firm-name {
    position: absolute;
    left: 0; top: 6px;
    font-size: 15px;
    font-weight: 700;
    color: var(--ink);
    white-space: nowrap;
  }
  .firm-address {
    position: absolute;
    left: 294px; top: 0;
    font-size: 10px;
    line-height: 13px;
    font-style: normal;
    color: var(--ink-soft);
  }
  .firm-phones {
    position: absolute;
    left: 422px; top: 0;
    font-size: 10px;
    line-height: 13px;
    color: var(--ink-soft);
  }
  .firm-phones li { list-style: none; display: flex; align-items: center; gap: 4px; }
  .firm-phones svg { width: 9px; height: 9px; fill: var(--ink); }

  .rule {
    position: absolute;
    left: 12px; right: 4px;
    height: 3px;
  }
  .rule svg { display: block; width: 100%; height: 3px; }
  .rule--top { top: 48px; }
  .rule--bottom { top: 709px; }

  .watermark {
    position: absolute;
    left: 117px; top: 235px;
    width: 296px; height: 296px;
  }
  .watermark svg { width: 100%; height: 100%; display: block; }

  .letter-body {
    position: absolute;
    left: 38px; top: 138px;
    width: 456px;
    font-size: 10.5px;
    line-height: 12.9px;
    color: var(--ink);
  }
  .letter-body p { margin-bottom: 12.9px; }
  .letter-body .salutation { margin-bottom: 13px; }
  .letter-body .signature { margin-top: 12.9px; padding-left: 2px; }

  .partners {
    position: absolute;
    left: 3px; top: 713px;
    font-size: 8.8px;
    line-height: 10.6px;
    color: var(--ink);
    white-space: nowrap;
  }
  .partners strong { font-weight: 700; }
</style>
</head>
<body>

  <section class="sheet sheet--blank">
    <header class="letterhead">
      <div class="firm-name">Pell &amp; Whitcombe, Attorneys-At-Law, LLP.</div>
      <address class="firm-address">1840 W. Magnolia Ave.<br>Fort Worth, TX 76104</address>
      <ul class="firm-phones">
        <li><svg viewBox="0 0 10 10"><path d="M2 0.5 L3.6 2.6 L2.8 3.6 Q3.8 5.8 6.4 7.2 L7.4 6.4 L9.5 8 L8.4 9.5 Q1.5 8 0.5 1.6 Z"/></svg>(817) 555-0142</li>
        <li><svg viewBox="0 0 10 10"><rect x="2.5" y="0.5" width="5" height="3"/><rect x="0.5" y="3.5" width="9" height="4" rx="1"/><rect x="2.5" y="6.5" width="5" height="3"/></svg>(817) 555-0187</li>
      </ul>
    </header>
    <div class="rule rule--top"><svg viewBox="0 0 520 3" preserveAspectRatio="none"><path d="M0 1.5 Q260 0 520 1.5 Q260 3 0 1.5 Z" fill="var(--rule)"/></svg></div>

    <div class="watermark" role="img" aria-label="Faint Texas star emblem watermark in a circle">
      <svg viewBox="0 0 296 296"><circle cx="148" cy="148" r="146" fill="var(--watermark)"/><circle cx="148" cy="148" r="138" fill="none" stroke="var(--watermark-edge)" stroke-width="3"/></svg>
    </div>

    <div class="rule rule--bottom"><svg viewBox="0 0 520 3" preserveAspectRatio="none"><path d="M0 1.5 Q260 0 520 1.5 Q260 3 0 1.5 Z" fill="var(--rule)"/></svg></div>
    <footer class="partners">
      Partners:<br>
      <strong>Daniel Pell</strong>, Managing Partner (Admitted in State of Texas, United States District Court (Eastern District of Texas), Fifth Circuit Court of Appeals)<br>
      <strong>Laura Jean Whitcombe</strong> (Admitted in the State of Texas)
    </footer>
  </section>

  <section class="sheet sheet--letter">
    <header class="letterhead">
      <div class="firm-name">Pell &amp; Whitcombe, Attorneys-At-Law, LLP.</div>
      <address class="firm-address">1840 W. Magnolia Ave.<br>Fort Worth, TX 76104</address>
      <ul class="firm-phones">
        <li><svg viewBox="0 0 10 10"><path d="M2 0.5 L3.6 2.6 L2.8 3.6 Q3.8 5.8 6.4 7.2 L7.4 6.4 L9.5 8 L8.4 9.5 Q1.5 8 0.5 1.6 Z"/></svg>(817) 555-0142</li>
        <li><svg viewBox="0 0 10 10"><rect x="2.5" y="0.5" width="5" height="3"/><rect x="0.5" y="3.5" width="9" height="4" rx="1"/><rect x="2.5" y="6.5" width="5" height="3"/></svg>(817) 555-0187</li>
      </ul>
    </header>
    <div class="rule rule--top"><svg viewBox="0 0 520 3" preserveAspectRatio="none"><path d="M0 1.5 Q260 0 520 1.5 Q260 3 0 1.5 Z" fill="var(--rule)"/></svg></div>

    <div class="watermark" role="img" aria-label="Faint Texas star emblem watermark in a circle">
      <svg viewBox="0 0 296 296"><circle cx="148" cy="148" r="146" fill="var(--watermark)"/><circle cx="148" cy="148" r="138" fill="none" stroke="var(--watermark-edge)" stroke-width="3"/></svg>
    </div>

    <div class="letter-body">
      <p class="salutation">Dear Addressee Name:</p>
      <p>Andipsum dipsum nostis nulpute magnissis niatie te molor adignis sequips uscipisit, sit vel ipsuscing ent lut lan ulla feugait augueraesto odolore doluptatio cons dolor sismodo luptatuero do od dolore magnim dolor auguero eu facilis ea core estrud eugiat velis ad tat dio odolor augue magna corting eugait enim venibh et, quatumsan hendre tincinisi tisisl dolute moloreet atem velesequat alit aliquat, vel dolore faciduis dolore dignis dolorper il eugiamconsed deliquamcon henis alis atum duis at.<br>
      Bore del ute faccum vercill aorper sent alit, venis autet, quipsustio eugue vero dolore velendre euis nos nonse dolessim illa feum dolor sumsan ectet lortincin vulputat amet, qui esto conulput acil in eugait vel essequam zzriusto diam, velit wissit autat.<br>
      Obore dolor incip ea conummy nulput vel ullan henisim am in ute erciliqui ex ent et, quis augiat, commod tis enis num delit laor acing elis dolorer se eugue feu facinci liquis aut lut nulluptat er sum zzrit vulla consequis accum incidunt iusci blaortio odoloreet pratum veliquatie modit, quat. Ut nummodo exercilisl iriliqu ipsusto dolesequat. Ut wisl in ute consequam ad diam vulputpat lan hent vel doloreet utat ver si.</p>
      <p>Vullaorem iusci blamcon seniamcommy nit iureetum dolore con ea faccum iureet prat. In utat acidunt nullum venismolum ing exer iusci bla augue magna consequi tem veliquis nostion utpat.<br>
      Nibh euipis esed ero doluptat. Ibh ex exeros exero dolesed dunt pratissi euis nismodipsum eu feuguerit ipisl incilla faccum am init praese tat velis augue corem iriliqu amconsequat. Magnim ipit in ea acincil esto et wisl esenim volenit lorem del ut aut la commy nibh eui tiniam iure mod tem vel ipisit, quis nonse-qui blan exerosto odolorem il irit num vel dolore et irit aute te dolestrud tin hent utet ut praestrud ea faccum venim venim il er iustion sequipsum quat.</p>
      <p>Do ea acilisis dolore min ercing endre consequat. Ero consequis ad euguerat, siscidunt laor sum iuscipis nullaoreet, velent ilit amconul laorperit lore diatum dui bla facipit irit alis ad dolorpe rostrud tem esse-quat praesequam, coreet ip er sim dit, velisim inciliquam, quis adigna feugue dolore et irillaor.<br>
      Adiam zzrit,</p>
      <p class="signature">Veliquatin Veraessi</p>
    </div>

    <div class="rule rule--bottom"><svg viewBox="0 0 520 3" preserveAspectRatio="none"><path d="M0 1.5 Q260 0 520 1.5 Q260 3 0 1.5 Z" fill="var(--rule)"/></svg></div>
    <footer class="partners">
      Partners:<br>
      <strong>Daniel Pell</strong>, Managing Partner (Admitted in State of Texas, United States District Court (Eastern District of Texas), Fifth Circuit Court of Appeals)<br>
      <strong>Laura Jean Whitcombe</strong> (Admitted in the State of Texas)
    </footer>
  </section>

</body>
</html>
```